Business card to promote business guidance

I need a card design to give to all my customers advertising a way to build a business exactly like the one they just bought from. I have an online store and will include one with each shipment. It should state the way to financial freedom and working for yourself

Target Market(s)

Young Entrepreneurs that want to start and don't know how

Industry/Entity Type

Business

Contact Information for Business Card

"You just bought from a successful company on Brindlemart. I have a unique business model, discovered by me, unlike any other that can make anyone successful. Follow me and message me for exactly the same model. If you ever wanted to work for yourself, I will teach you how. It's not a pipe dream, allow me to guide you out of the box."

Colors
85abd2

Requirements
Must have
• website www.dorianwelkby.example
instagram @thedorianwelkby

```html
<!DOCTYPE html>
<html lang="en">
<head>
<meta charset="utf-8">
<title>Dorian Welkby – Thank You Card</title>
<link href="https://fonts.googleapis.com/css2?family=Open+Sans:wght@400;600;700&display=swap" rel="stylesheet">
<style>
  :root {
    --brand-blue: #85abd2;
    --ink: #444444;
    --frame-line: #8a8a8a;
    --paper: #ffffff;
  }
  * { margin: 0; padding: 0; box-sizing: border-box; }
  html, body {
    width: 1200px; height: 407px; overflow: hidden;
    background: var(--paper);
    font-family: "Open Sans", sans-serif;
  }
  .canvas { position: relative; width: 1200px; height: 407px; }

  /* Front side */
  .card-front {
    position: absolute; left: 0; top: 0; width: 568px; height: 407px;
    background: var(--brand-blue);
  }
  .card-front__panel {
    position: absolute; left: 16px; top: 11px; width: 538px; height: 385px;
    background: var(--paper);
    border: 1px solid var(--frame-line);
  }
  .logo-placeholder {
    position: absolute; left: 212px; top: 27px; width: 114px; height: 114px;
    border-radius: 50%; background: var(--brand-blue);
    display: flex; align-items: center; justify-content: center;
    color: var(--paper); font-size: 22px; line-height: 22px; text-align: center;
    font-family: Arial, Helvetica, sans-serif;
  }
  .thanks {
    position: absolute; left: 0; width: 100%; text-align: center;
    color: var(--brand-blue); font-weight: 700;
  }
  .thanks--main { top: 190px; font-size: 60px; line-height: 70px; letter-spacing: 1px; }
  .thanks--sub { top: 254px; font-size: 42px; line-height: 50px; letter-spacing: 0.5px; }

  /* Back side */
  .card-back { position: absolute; left: 610px; top: 0; width: 568px; height: 407px; }
  .brace { position: absolute; top: 38px; width: 34px; height: 230px; }
  .brace--left { left: 27px; }
  .brace--right { left: 513px; }
  .message {
    position: absolute; left: 40px; width: 504px; top: 48px;
    text-align: center; color: var(--ink);
    font-size: 14px; line-height: 22.6px; letter-spacing: 0.4px;
  }
  .message p + p { margin-top: 22px; }
  .signature {
    position: absolute; left: 0; width: 584px; top: 276px; text-align: center;
    color: var(--ink); font-size: 24px; font-weight: 700; letter-spacing: 4px; word-spacing: 10px;
  }
  .contact {
    position: absolute; top: 335px; display: flex; align-items: center; gap: 12px;
    color: var(--ink); font-size: 13.5px; letter-spacing: 0.4px;
  }
  .contact--web { left: 39px; }
  .contact--social { left: 363px; }
  .contact__mark {
    width: 29px; height: 29px; border: 2.5px solid var(--ink); border-radius: 6px;
  }
  .contact__globe { width: 31px; height: 31px; }
  .card-back__band {
    position: absolute; left: 0; top: 375px; width: 568px; height: 32px;
    background: var(--brand-blue);
  }
</style>
</head>
<body>
<main class="canvas">
  <section class="card-front">
    <div class="card-front__panel">
      <div class="logo-placeholder">YOUR<br>LOGO<br>HERE</div>
      <div class="thanks thanks--main">Thank you</div>
      <div class="thanks thanks--sub">for your order!</div>
    </div>
  </section>

  <section class="card-back">
    <svg class="brace brace--left" viewBox="0 0 34 230" aria-hidden="true">
      <path d="M33 2 H26 Q15 2 15 20 V95 Q15 108 3 114 Q15 120 15 133 V210 Q15 228 26 228 H33"
            fill="none" stroke="var(--brand-blue)" stroke-width="3"/>
    </svg>
    <svg class="brace brace--right" viewBox="0 0 34 230" aria-hidden="true">
      <path d="M1 2 H8 Q19 2 19 20 V95 Q19 108 31 114 Q19 120 19 133 V210 Q19 228 8 228 H1"
            fill="none" stroke="var(--brand-blue)" stroke-width="3"/>
    </svg>

    <div class="message">
      <p>Dear Customer,</p>
      <p>You just bought from a successful company on Brindlemart.<br>
      I have a unique business model, discovered by me, unlike any<br>
      other that can make anyone successful.&nbsp; Follow me and mes-<br>
      sage me for exactly the same model. If you ever wanted to<br>
      work for yourself, I will teach you how.</p>
      <p>It's not a pipe dream, allow me to guide you out of the box.</p>
    </div>

    <div class="signature">DORIAN WELKBY</div>

    <div class="contact contact--web">
      <span class="contact__mark" aria-hidden="true"></span>
      <span>www.dorianwelkby.example</span>
    </div>
    <div class="contact contact--social">
      <svg class="contact__globe" viewBox="0 0 32 32" aria-hidden="true">
        <g fill="none" stroke="var(--ink)" stroke-width="2">
          <circle cx="16" cy="16" r="14"/>
          <ellipse cx="16" cy="16" rx="6" ry="14"/>
          <line x1="16" y1="2" x2="16" y2="30"/>
          <line x1="2" y1="16" x2="30" y2="16"/>
          <path d="M5 8.5 H27 M5 23.5 H27"/>
        </g>
      </svg>
      <span>@thedorianwelkby</span>
    </div>

    <div class="card-back__band"></div>
  </section>
</main>
</body>
</html>
```